Tollbury Malt Keller Beer Bottle Label #1

A beer bottle label is required for TMK's first beer that will go on sale later this year.
It is hoped that an on-going relationship will be formed with the successful designer.
Designs for glasses, packaging, t-shirts etc will also be required later this year.
Designs should reflect the local origin of the brewery and project an image of tradition and quality.
Designs should be simple, clean, classic and classy.
Designs should not be loud, bright, crazy or busy.
Design should include an element that can be used as brewery logo.
'Malt Keller' to be prominent, 'Tollbury' to be discreet.
Name of first beer to be Tollmo-Dunkel - label shall be easily adapted for different beers e.g. Tollmo-Weiss.
Deliverables include a smaller text only label for back of the bottle.

***I also need a logo that goes with my label design. So whoever submitted a logo that I like will be selected as the 2nd place winner.

Please refer to the attachment on this brief.

Requirements
Must have
• See uploaded design brief.
Nice to have
Should not have

```html
<!DOCTYPE html>
<html lang="en">
<head>
<meta charset="utf-8">
<title>Tollbury Malt Keller – Tollmo-Dunkel label</title>
<link href="https://fonts.googleapis.com/css2?family=Josefin+Sans:wght@300;400&family=Kaushan+Script&family=Crimson+Text&display=swap" rel="stylesheet">
<style>
  :root {
    --backdrop: #d3cdc1;
    --cream: #ede6da;
    --brand-red: #7d1d22;
    --ink-dark: #2f3642;

    --slate-frame: #7a8496;
    --slate-top: #bab6ae;
    --slate-disc: #5b6b86;
    --slate-ring: #8b1a1a;
    --slate-script: #aaa6a0;
    --slate-title: #2b3a5a;

    --olive-frame: #b9b2a6;
    --olive-top: #6d6d69;
    --olive-disc: #a39a3c;
    --olive-ring: #bdb6aa;
    --olive-script: #8e8a35;
    --olive-title: #383838;

    --stone-frame: #b4aa92;
    --stone-top: #7f7f7d;
    --stone-disc: #a9a59e;
    --stone-ring: #586a86;
    --stone-script: #7a7a78;
    --stone-title: #3c4a62;
  }
  * { margin: 0; padding: 0; box-sizing: border-box; }
  html, body { width: 1200px; height: 491px; overflow: hidden; background: var(--backdrop); }
  .canvas { position: relative; width: 1200px; height: 491px; }

  .label {
    position: absolute; top: 56px; width: 220px; height: 365px;
    border: 7px solid var(--frame); background: var(--top);
  }
  .label--slate { left: 82px; --frame: var(--slate-frame); --top: var(--slate-top); --disc: var(--slate-disc); --ring: var(--slate-ring); --script: var(--slate-script); --title: var(--slate-title); }
  .label--olive { left: 366px; --frame: var(--olive-frame); --top: var(--olive-top); --disc: var(--olive-disc); --ring: var(--olive-ring); --script: var(--olive-script); --title: var(--olive-title); }
  .label--stone { left: 899px; --frame: var(--stone-frame); --top: var(--stone-top); --disc: var(--stone-disc); --ring: var(--stone-ring); --script: var(--stone-script); --title: var(--stone-title); }

  .label__stripes {
    position: absolute; left: 0; right: 0; top: 106px; height: 24px;
    background: repeating-linear-gradient(to bottom, var(--frame) 0 3px, var(--cream) 3px 7px);
  }
  .label__panel { position: absolute; left: 0; right: 0; top: 130px; bottom: 0; background: var(--cream); }

  .label__disc {
    position: absolute; left: 50%; top: -24px; width: 94px; height: 94px; margin-left: -47px;
    border-radius: 50%; background: var(--disc); border: 6px solid var(--ring);
  }

  .label__maker {
    position: absolute; left: 50%; top: 76px; width: 110px; margin-left: -55px;
    font-family: "Josefin Sans", sans-serif; font-weight: 400; font-size: 11px; line-height: 1.2;
    text-align: center; color: var(--brand-red); letter-spacing: 0.04em; text-transform: uppercase;
  }

  .label__beer { position: absolute; left: 0; right: 0; top: 148px; text-align: center; font-weight: normal; }
  .label__beer-name {
    display: block; font-family: "Josefin Sans", sans-serif; font-weight: 300;
    font-size: 44px; line-height: 1; color: var(--title);
  }
  .label__beer-style {
    display: block; margin-top: 0; font-family: "Kaushan Script", cursive;
    font-size: 54px; line-height: 1.05; color: var(--script); transform: skewX(-6deg);
  }

  .label__brewery { position: absolute; left: 0; right: 0; top: 280px; text-align: center; color: var(--ink-dark); font-family: "Josefin Sans", sans-serif; }
  .label__brewery-name { display: block; font-size: 20px; font-weight: 300; letter-spacing: 0.01em; }
  .label__brewery-town { display: block; font-size: 14px; font-weight: 300; margin-top: 1px; }

  .label__facts {
    position: absolute; left: 18px; right: 18px; bottom: 9px;
    display: flex; justify-content: space-between;
    font-family: "Crimson Text", serif; font-size: 10px; color: var(--ink-dark);
  }

  .brand-mark {
    position: absolute; left: 663px; top: 150px; width: 180px; text-align: center;
  }
  .brand-mark__badge {
    width: 34px; height: 34px; margin: 0 auto 14px; border-radius: 50%; background: var(--brand-red);
  }
  .brand-mark__name {
    font-family: "Josefin Sans", sans-serif; font-weight: 400; font-size: 26px; line-height: 1.2;
    letter-spacing: 0.05em; text-transform: uppercase; color: var(--brand-red);
  }
</style>
</head>
<body>
<main class="canvas">

  <article class="label label--slate">
    <div class="label__stripes"></div>
    <div class="label__panel"></div>
    <div class="label__disc"></div>
    <p class="label__maker">Tollbury<br>Malt Keller</p>
    <h2 class="label__beer"><span class="label__beer-name">Tollmo</span><span class="label__beer-style">Dunkel</span></h2>
    <p class="label__brewery"><span class="label__brewery-name">MALT KELLER</span><span class="label__brewery-town">Tollbury</span></p>
    <p class="label__facts"><span>ABV 4.6%</span><span>2.3 Units</span><span>500ml</span></p>
  </article>

  <article class="label label--olive">
    <div class="label__stripes"></div>
    <div class="label__panel"></div>
    <div class="label__disc"></div>
    <p class="label__maker">Tollbury<br>Malt Keller</p>
    <h2 class="label__beer"><span class="label__beer-name">Tollmo</span><span class="label__beer-style">Dunkel</span></h2>
    <p class="label__brewery"><span class="label__brewery-name">MALT KELLER</span><span class="label__brewery-town">Tollbury</span></p>
    <p class="label__facts"><span>ABV 4.6%</span><span>2.3 Units</span><span>500ml</span></p>
  </article>

  <div class="brand-mark">
    <div class="brand-mark__badge"></div>
    <p class="brand-mark__name">Tollbury<br>Malt Keller</p>
  </div>

  <article class="label label--stone">
    <div class="label__stripes"></div>
    <div class="label__panel"></div>
    <div class="label__disc"></div>
    <p class="label__maker">Tollbury<br>Malt Keller</p>
    <h2 class="label__beer"><span class="label__beer-name">Tollmo</span><span class="label__beer-style">Dunkel</span></h2>
    <p class="label__brewery"><span class="label__brewery-name">MALT KELLER</span><span class="label__brewery-town">Tollbury</span></p>
    <p class="label__facts"><span>ABV 4.6%</span><span>2.3 Units</span><span>500ml</span></p>
  </article>

</main>
</body>
</html>
```